Marine Business Card

We install Lighting, Sound, Video, PA Systems to hotels, nightclubs, Restaurants, Cruise Ships.

Target Market(s)

We want to focus on the Marine or Maritime/Cruise industry. Passenger ships and cruise liners are the companies we want to appeal to

Industry/Entity Type

Business

Contact Information for Business Card

Mark Tilbury
Managing Director
Harbourne Vista Audio Marine Ltd

Requirements
Must have
• Office: 01632 960482
Mobile: 07700 900317
mark@harbournevistaaudio.co.uk
www.harbournevistaaudio.co.uk

```html
<!DOCTYPE html>
<html lang="en">
<head>
<meta charset="utf-8">
<title>Harbourne Vista Audio – Business Card</title>
<link rel="stylesheet" href="https://fonts.googleapis.com/css2?family=Open+Sans:wght@400;600;700&family=Alegreya+Sans+SC:wght@800&display=swap">
<style>
  :root {
    --page: #ffffff;
    --card: #ffffff;
    --sea-light: #fbfbfb;
    --sea-mid: #eeeeee;
    --land: #d4d4d4;
    --brand-blue: #2b2f8c;
    --brand-blue-light: #3a55a6;
    --ink-grey: #444444;
    --text-grey: #555555;
  }
  * { margin: 0; padding: 0; box-sizing: border-box; }
  html, body { width: 1200px; height: 1000px; overflow: hidden; background: var(--page); }
  .canvas { position: relative; width: 1200px; height: 1000px; }

  .card {
    position: absolute;
    overflow: hidden;
    background: linear-gradient(180deg, var(--sea-light) 0%, var(--card) 55%, var(--sea-mid) 100%);
    box-shadow: 0 2px 6px rgba(0,0,0,.25);
  }
  .card--front { left: 56px; top: 30px; width: 1084px; height: 636px; }
  .card--back { left: 640px; top: 700px; width: 500px; height: 280px; }

  .map-area {
    position: absolute;
    background: radial-gradient(ellipse at 45% 50%, var(--land) 0%, rgba(212,212,212,.55) 45%, rgba(212,212,212,0) 75%);
  }
  .card--front .map-area { left: 0; top: 0; width: 720px; height: 510px; }
  .card--back .map-area { left: 120px; top: 60px; width: 260px; height: 170px; }

  .brand-band {
    position: absolute;
    background: linear-gradient(180deg, var(--brand-blue) 0%, var(--brand-blue-light) 50%, var(--brand-blue) 100%);
  }
  .card--front .brand-band { right: 0; top: 0; width: 90px; height: 346px; }
  .card--back .brand-band { left: 0; top: 0; width: 34px; height: 160px; }

  .brand-name {
    position: absolute;
    font-family: "Open Sans", sans-serif;
    font-weight: 700;
    color: var(--brand-blue);
    line-height: 1;
    letter-spacing: -0.5px;
  }
  .card--front .brand-name { right: 110px; top: 256px; text-align: right; font-size: 46px; }
  .card--back .brand-name { left: 46px; top: 24px; font-size: 22px; }

  .services {
    position: absolute;
    left: 0; right: 0; top: 542px;
    display: flex; justify-content: center; gap: 20px;
    font-family: "Alegreya Sans SC", sans-serif;
    font-weight: 800;
    font-size: 26px;
  }
  .services .accent { color: var(--brand-blue); }
  .services .neutral { color: var(--ink-grey); }

  .contact {
    position: absolute;
    left: 330px; top: 56px; width: 160px;
    font-family: "Open Sans", sans-serif;
    font-size: 8.5px;
    color: var(--text-grey);
    line-height: 1.35;
  }
  .contact-group { display: flex; gap: 8px; margin-bottom: 12px; }
  .contact-group svg { flex: none; margin-top: 2px; }
  .contact-label { font-weight: 700; color: var(--brand-blue); letter-spacing: .5px; text-transform: uppercase; }
  .contact-name { font-weight: 700; color: var(--ink-grey); font-size: 10px; }
</style>
</head>
<body>
<div class="canvas">

  <section class="card card--front">
    <div class="map-area" role="img" aria-label="Faint grey map of South-East Asia, Australia and New Zealand over a pale sea surface"></div>
    <div class="brand-band"></div>
    <div class="brand-name">HARBOURNE<br>VISTA AUDIO</div>
    <div class="services">
      <span class="accent">Lighting Systems</span>
      <span class="neutral">Sound Systems</span>
      <span class="accent">Video Systems</span>
      <span class="neutral">Bespoke Systems</span>
    </div>
  </section>

  <section class="card card--back">
    <div class="map-area" role="img" aria-label="Faint grey map of the Americas and Africa over a pale sea surface"></div>
    <div class="brand-band"></div>
    <div class="brand-name">HARBOURNE<br>VISTA AUDIO</div>
    <div class="contact">
      <div class="contact-group">
        <svg width="9" height="9" viewBox="0 0 10 10" aria-hidden="true"><path d="M5 0a3.5 3.5 0 0 0-3.5 3.5C1.5 6 5 10 5 10s3.5-4 3.5-6.5A3.5 3.5 0 0 0 5 0z" fill="#777"/></svg>
        <div>
          <div class="contact-name">Mark Tilbury</div>
          <div>Managing Director</div>
          <div class="contact-label">Address</div>
          <div>14 Quayside Row, Fleetwood,<br>Lancashire, FY7 6QB</div>
        </div>
      </div>
      <div class="contact-group">
        <svg width="9" height="9" viewBox="0 0 10 10" aria-hidden="true"><rect x="2" y="0.5" width="6" height="9" rx="1" fill="none" stroke="#777"/></svg>
        <div>
          <div class="contact-label">Telephone</div>
          <div>office 01632 960482</div>
          <div>mobile 07700 900317</div>
        </div>
      </div>
      <div class="contact-group">
        <svg width="9" height="9" viewBox="0 0 10 10" aria-hidden="true"><circle cx="5" cy="5" r="4.3" fill="none" stroke="#777"/></svg>
        <div>
          <div class="contact-label">Web</div>
          <div>mark@harbournevistaaudio.co.uk</div>
          <div>www.harbournevistaaudio.co.uk</div>
        </div>
      </div>
    </div>
  </section>

</div>
</body>
</html>
```